Telecommunications/Power civil contractor needs business card design

Were a new telecommunications/power underground civil contractor that is looking for a new business card design. Our company colours are silver or grey and orange. Feel free to use the white background logo or the black background logo.

Target Market(s)

Local contractors, utility companies, private sector mining/energy companies, developers.

Industry/Entity Type

Telecommunications

Contact Information for Business Card

Each card will need the following info:
Persons name:
Title:
E-mail:
Phone number:
Shop Address:
Mailing Address:

Requirements
Must have
• Each card will need the following info:
• Persons name:
• Title:
• E-mail:
• Phone number:
• Shop Address:
• Mailing Address:

```html
<!DOCTYPE html>
<html lang="en">
<head>
<meta charset="UTF-8">
<title>Business Card – Trenchline Civil Inc</title>
<link href="https://fonts.googleapis.com/css2?family=Open+Sans:wght@400;600;800&display=swap" rel="stylesheet">
<style>
  :root {
    --page-bg: #e6e4e5;
    --card-black: #060708;
    --accent-orange: #f15a24;
    --silver-light: #fbfbfb;
    --silver-mid: #e4e5e7;
    --ink: #141414;
    --ink-soft: #3a3a3a;
  }
  html, body {
    margin: 0;
    width: 1200px;
    height: 1200px;
    overflow: hidden;
    background: var(--page-bg);
  }
  .canvas {
    width: 1200px;
    height: 1200px;
    display: flex;
    align-items: center;
    justify-content: center;
  }
  .business-card {
    width: 1000px;
    height: 571px;
    filter: drop-shadow(0 10px 18px rgba(0,0,0,0.25));
  }
  .brand-name {
    font-family: "Open Sans", sans-serif;
    font-weight: 800;
    fill: var(--accent-orange);
    letter-spacing: 2px;
  }
  .person-name {
    font-family: "Open Sans", sans-serif;
    font-weight: 800;
    font-size: 38px;
    fill: var(--ink);
  }
  .person-title {
    font-family: "Open Sans", sans-serif;
    font-weight: 400;
    font-size: 20px;
    fill: var(--ink-soft);
  }
  .contact-line {
    font-family: "Open Sans", sans-serif;
    font-weight: 400;
    font-size: 20px;
    fill: var(--ink-soft);
  }
  .icon-disc { fill: var(--ink); }
  .icon-mark { fill: #ffffff; }
</style>
</head>
<body>
<main class="canvas">
  <svg class="business-card" viewBox="0 0 1000 571" xmlns="http://www.w3.org/2000/svg" aria-label="Business card for Trenchline Civil Inc">
    <defs>
      <clipPath id="card-shape">
        <rect x="0" y="0" width="1000" height="571" rx="48" ry="48"/>
      </clipPath>
      <linearGradient id="silver-finish" x1="0" y1="0" x2="1" y2="0.3">
        <stop offset="0" stop-color="var(--silver-mid)"/>
        <stop offset="0.35" stop-color="var(--silver-light)"/>
        <stop offset="0.55" stop-color="#d9dadc"/>
        <stop offset="0.75" stop-color="var(--silver-light)"/>
        <stop offset="1" stop-color="var(--silver-mid)"/>
      </linearGradient>
    </defs>

    <g clip-path="url(#card-shape)">
      <rect class="card-body" x="0" y="0" width="1000" height="571" fill="url(#silver-finish)"/>
      <path class="header-band" d="M0 0 H1000 V80 C650 130 300 250 0 330 Z" fill="var(--card-black)"/>
      <path class="accent-swoosh" d="M330 248 C600 168 800 116 1000 92 V114 C800 136 600 186 330 248 Z" fill="var(--accent-orange)"/>
    </g>

    <text class="brand-name" x="45" y="190" font-size="52">TRENCHLINE</text>
    <text class="brand-name" x="47" y="232" font-size="28">CIVIL INC</text>

    <text class="person-name" x="70" y="372">JOHN DOE</text>
    <text class="person-title" x="72" y="400">Director</text>

    <g class="contact-phone">
      <circle class="icon-disc" cx="84" cy="438" r="10"/>
      <path class="icon-mark" d="M79 434 q5 -4 10 0 l-1 2 h-8 z M80 438 h8 v4 h-8 z"/>
      <text class="contact-line" x="104" y="445">1-234-567890</text>
    </g>
    <g class="contact-email">
      <circle class="icon-disc" cx="84" cy="471" r="10"/>
      <rect class="icon-mark" x="78" y="467" width="12" height="8" rx="1"/>
      <text class="contact-line" x="104" y="478">john@companyname.com</text>
    </g>
    <g class="contact-mailing">
      <circle class="icon-disc" cx="84" cy="516" r="10"/>
      <circle class="icon-mark" cx="84" cy="516" r="3.5"/>
      <text class="contact-line" x="104" y="511">Dummy city</text>
      <text class="contact-line" x="104" y="537">Dummy Country Land Dummy</text>
    </g>

    <g class="contact-shop">
      <text class="contact-line" x="910" y="300" text-anchor="end">123 Dummy Street</text>
      <text class="contact-line" x="940" y="330" text-anchor="end">Dummy Centre, Dummy 12345</text>
      <circle class="icon-disc" cx="929" cy="293" r="11"/>
      <path class="icon-mark" d="M929 286 l6 6 h-2 v6 h-8 v-6 h-2 z"/>
    </g>
  </svg>
</main>
</body>
</html>
```